Bright Path Attorneys Billboard Design for Personal Injury Law Firm

Need a billboard design that we can use for different versions. 1400px X 400px jpeg or png
I have attached the logo and the attorney for the billboard. Attorney Marla Benning
Here is a link to our current website brightpathlegalgroup.example

HEADLINE: HIT BY A TRUCK?
SUBHEAD: NO FEE. BIG FIGHT.
877-GRANTLY

HEADLINE: ACCIDENT?
SUBHEAD: NO FEE, UNLESS WE WIN!
877-GRANTLY

HEADLINE: BIG TRUCK. BIG CASE.
SUBHEAD: YOU PAY $0 UPFRONT
877-GRANTLY

Target Market(s)

People in Car Accident

Industry/Entity Type

Personal Injury Attorneys

```html
<!DOCTYPE html>
<html lang="en">
<head>
<meta charset="utf-8">
<title>Bright Path Attorneys Billboard</title>
<link href="https://fonts.googleapis.com/css2?family=Poppins:wght@500;600;800&display=swap" rel="stylesheet">
<style>
  :root {
    --stage: #808185;
    --navy-dark: #121a24;
    --navy: #15294d;
    --green: #76c044;
    --white: #ffffff;
    --ink: #1d1d1b;
    --charcoal: #474747;
    --photo-light: #c8a27a;
    --photo-dark: #1c2746;
  }
  * { box-sizing: border-box; margin: 0; padding: 0; }
  html, body {
    width: 1200px; height: 400px; overflow: hidden;
    background: var(--stage);
    font-family: "Poppins", sans-serif;
  }
  .billboard {
    position: absolute; left: 0; top: 28px;
    width: 1200px; height: 343px;
    background: var(--white);
    overflow: hidden;
  }
  .sky {
    position: absolute; left: 0; top: 0; width: 100%; height: 232px;
    background: linear-gradient(90deg, var(--navy-dark) 0%, #17233a 40%, var(--navy) 100%);
  }
  .rule {
    position: absolute; left: 0; top: 231px; width: 100%; height: 6px;
    background: var(--green);
  }
  .attorney-photo {
    position: absolute; left: 52px; top: 9px; width: 300px; height: 334px;
    border-radius: 150px 150px 0 0;
    background: linear-gradient(180deg, var(--photo-light) 0%, #a47c58 35%, var(--photo-dark) 70%, var(--photo-dark) 100%);
  }
  .name-tag {
    position: absolute; left: 0; top: 231px; width: 220px; height: 45px;
    background: var(--green);
    display: flex; align-items: center; justify-content: center;
    font-weight: 500; font-size: 24px; color: var(--ink); letter-spacing: -0.5px;
  }
  .headline {
    position: absolute; left: 278px; top: 38px; width: 886px;
    font-weight: 800; font-size: 108px; line-height: 1;
    letter-spacing: -4px; white-space: nowrap; color: var(--green);
    text-align: right;
  }
  .headline .accent { color: var(--white); }
  .subhead {
    position: absolute; left: 380px; top: 150px; width: 690px; text-align: center;
    font-weight: 500; font-size: 54px; line-height: 1; letter-spacing: -1.5px;
    color: var(--white); white-space: nowrap;
  }
  .phone {
    position: absolute; left: 372px; top: 247px; width: 420px; text-align: center;
    font-weight: 600; font-size: 62px; line-height: 1; letter-spacing: -2.5px;
    color: var(--charcoal); white-space: nowrap;
  }
  .phone .word { color: var(--green); }
  .divider {
    position: absolute; left: 822px; top: 244px; width: 2px; height: 89px;
    background: var(--green);
  }
  .firm {
    position: absolute; left: 852px; top: 258px; width: 310px; height: 62px;
    display: flex; align-items: center; gap: 12px;
  }
  .firm-dot { width: 30px; height: 30px; border-radius: 50%; background: var(--green); flex: none; }
  .firm-name {
    font-weight: 600; font-size: 24px; line-height: 1.05; color: var(--charcoal);
    letter-spacing: -0.3px;
  }
</style>
</head>
<body>
  <main class="billboard">
    <div class="sky"></div>
    <div class="rule"></div>
    <div class="attorney-photo" role="img" aria-label="Portrait of attorney Marla Benning in a navy blazer, arms crossed"></div>
    <div class="name-tag">Marla Benning</div>
    <h1 class="headline">HIT BY A <span class="accent">TRUCK</span>?</h1>
    <p class="subhead">NO FEE. BIG FIGHT.</p>
    <p class="phone">877-<span class="word">GRANTLY</span></p>
    <div class="divider"></div>
    <div class="firm">
      <span class="firm-dot"></span>
      <span class="firm-name">Bright Path Attorneys</span>
    </div>
  </main>
</body>
</html>
```